Gymnastics Award Design Needed--for kids

Need a gymnastics certificate or award designed. Will be printed on a piece of 8.5x11 paper. The award will be celebrating the gymnast learning a new skill in gymnastics. So it should be fun, but still look "official". Needs to look good hanging on a gymnast's bedroom wall.

It should say "The Aerial Cartwheel Club"
I will be using this design to change it based on the skill.

My main colors are:
#34475D
#E1467A
#7555A4

So should use those, but can add others

My website is tumblenestpro.com so you can see the look/feel.

Target Market(s)

Main audience will be girls ages 5-12, but will also be used by slightly older girls and boys. So needs to be fun, not too gender specific.

Industry/Entity Type

Learning

Requirements
Must have
• The following will need to go on the certificate:
• * Name of Skill
• * Image of Skill
• * Gymnast's Name
• * my logo
• * Gym's Logo
• * Gym's Name
• Optional: Date

```html
<!DOCTYPE html>
<html lang="en">
<head>
<meta charset="utf-8">
<title>The Aerial Cartwheel Club Certificate</title>
<link rel="stylesheet" href="https://fonts.googleapis.com/css2?family=Stardos+Stencil:wght@700&family=Pinyon+Script&family=Quicksand:wght@400;500&display=swap">
<style>
  :root {
    --paper: #ffffff;
    --frame-pink: #ee2aa6;
    --title-pink: #ef2aa8;
    --dot-lilac: #d9d6f3;
    --ink: #111111;
    --violet: #5548e6;
    --brand-pink: #e64bb0;
    --figure-purple: #a13de0;
    --figure-skin: #f0c9a2;
  }
  * { margin: 0; padding: 0; box-sizing: border-box; }
  html, body { width: 848px; height: 1200px; overflow: hidden; background: var(--paper); }
  .certificate {
    position: relative; width: 848px; height: 1200px; background: var(--paper);
    border: 6px dotted var(--dot-lilac);
  }
  .frame { position: absolute; left: 0; top: 0; }
  .heading-the {
    position: absolute; top: 34px; width: 100%; text-align: center;
    font-family: "Pinyon Script", cursive; font-size: 66px; color: var(--ink); line-height: 1;
  }
  .club-title {
    position: absolute; top: 112px; width: 100%; text-align: center;
    font-family: "Stardos Stencil", "Stencil", sans-serif; font-weight: 700;
    color: var(--title-pink); font-size: 106px; line-height: 108px; letter-spacing: 1px;
  }
  .skill-illustration {
    position: absolute; left: 172px; top: 476px; width: 504px; height: 162px;
    background: linear-gradient(180deg, #ffffff 0%, #f6ecfb 60%, #eadff4 100%);
    border-bottom: 3px solid #c4c4c4;
  }
  .script { font-family: "Pinyon Script", cursive; color: var(--ink); line-height: 1; position: absolute; }
  .skill-name { top: 680px; width: 100%; text-align: center; font-size: 44px; }
  .rule { position: absolute; height: 2px; background: var(--ink); }
  .rule-skill { left: 192px; top: 745px; width: 464px; }
  .presented { left: 48px; top: 794px; font-size: 46px; color: var(--violet); }
  .rule-name { left: 352px; top: 833px; width: 444px; }
  .presenter { top: 856px; width: 100%; text-align: center; font-size: 44px; }
  .gym-mark { position: absolute; left: 58px; top: 960px; width: 250px; text-align: center; }
  .gym-mark .dot { display: block; width: 72px; height: 72px; border-radius: 50%; background: var(--violet); margin: 0 auto 18px; }
  .gym-mark .gym-name { font-family: "Quicksand", sans-serif; font-size: 31px; color: var(--ink); letter-spacing: 1px; }
  .brand-mark {
    position: absolute; left: 444px; top: 1005px; width: 340px;
    font-family: "Quicksand", sans-serif; font-size: 36px; font-weight: 400;
    color: var(--brand-pink); letter-spacing: 1px; white-space: nowrap;
  }
  .date { left: 262px; top: 1112px; font-size: 36px; }
  .rule-date { left: 368px; top: 1146px; width: 214px; }
</style>
</head>
<body>
  <main class="certificate">
    <svg class="frame" width="836" height="1188" viewBox="6 6 836 1188" aria-hidden="true">
      <rect x="22" y="22" width="804" height="1156" fill="none" stroke="var(--frame-pink)" stroke-width="3"/>
      <g fill="var(--frame-pink)">
        <rect x="20" y="20" width="76" height="7"/><rect x="20" y="20" width="7" height="76"/>
        <rect x="752" y="20" width="76" height="7"/><rect x="821" y="20" width="7" height="76"/>
        <rect x="20" y="1173" width="76" height="7"/><rect x="20" y="1104" width="7" height="76"/>
        <rect x="752" y="1173" width="76" height="7"/><rect x="821" y="1104" width="7" height="76"/>
      </g>
    </svg>

    <div class="heading-the">The</div>
    <h1 class="club-title">AERIAL<br>CARTWHEEL<br>CLUB</h1>

    <div class="skill-illustration" role="img" aria-label="Sequence of a gymnast in a purple leotard performing an aerial cartwheel, shown in five stages"></div>

    <div class="script skill-name">Name of Skill</div>
    <div class="rule rule-skill"></div>

    <div class="script presented">Presented To:</div>
    <div class="rule rule-name"></div>

    <div class="script presenter">by Ridgeline Gymnastics Gym.</div>

    <div class="gym-mark">
      <span class="dot"></span>
      <span class="gym-name">Ridgeline Gym</span>
    </div>

    <div class="brand-mark">TUMBLENEST PRO</div>

    <div class="script date">Date:</div>
    <div class="rule rule-date"></div>
  </main>
</body>
</html>
```